Business cards for Norwegian software consultancy business

We are in need of business cards for our Norwegian consultancy company.
“Talvik Brensor AS” specializes in software development, architecture and agile methodology, providing mostly on-site services at customers.
The cards should reflect a certain level of business professionalism with an elegant touch, while paying tribute to our modern and technological heritage. Our logo should be featured, as well as room for basic information about the cardholder and legal information of the company (company name, address and VAT number).
We would like our cards to reflect that we are a modern consulting company. It should present a professional image that people will remember. The texture and color pallette should reflect our professionalism and reliability, so we prefer a light color pallette with colors such as gray, white, blue and black. The number of colors used should however not be overwhelming, with the text being distinct and readable.
We are open to untraditional layouts and playful designs as long as they communicate the intent stated above.
You could also take a look at our website http://www.brensor.no for input on our visual profile.
Our logo is attached in the form of vectors and rasterized PNG. Please comment if you would like the black-white and/or inverted versions as well.
Architecture
Company information:
Talvik Brensor AS
Lindeholtveien 7, 3142 Vestskogen
461 82 915
info@brensor.no
www.brensor.no
Employee information:
Full name
Title
Email
Phone

```html
<!DOCTYPE html>
<html lang="no">
<head>
<meta charset="utf-8">
<title>Talvik Brensor AS – Business Cards</title>
<link rel="stylesheet" href="https://fonts.googleapis.com/css2?family=Arimo:wght@400;700&family=Roboto+Condensed:wght@400&display=swap">
<style>
  :root {
    --stage: #5f6466;
    --card-white: #ffffff;
    --blue-light: #8db9dc;
    --blue-mid: #6fa6d3;
    --blue-deep: #5e9acb;
    --ink: #111417;
    --text-blue: #6a9fd0;
    --title-blue: #3f7fc0;
    --band-text: #8ab6de;
  }
  * { box-sizing: border-box; margin: 0; padding: 0; }
  html, body {
    width: 1200px; height: 900px; overflow: hidden;
    background: var(--stage);
    font-family: "Arimo", Arial, sans-serif;
  }
  .sheet {
    position: relative; width: 1200px; height: 900px;
  }
  .card {
    position: absolute; left: 230px;
    width: 740px; height: 390px;
    border-radius: 34px;
    overflow: hidden;
  }
  /* Back: contact card */
  .card--contact { top: 40px; background: var(--card-white); }
  .contact-blue {
    position: absolute; left: 0; right: 0; bottom: 0; height: 205px;
    background: linear-gradient(180deg, var(--blue-light), var(--blue-deep));
  }
  .contact-info {
    position: absolute; left: 330px; top: 40px;
    color: var(--text-blue); font-size: 17px; line-height: 1.25;
  }
  .contact-name { font-size: 18px; }
  .contact-title { color: var(--title-blue); font-weight: 700; font-size: 18px; margin-bottom: 6px; }
  .contact-line { display: flex; align-items: center; gap: 10px; }
  .contact-line svg { width: 16px; height: 16px; flex: none; }
  .contact-address { padding-left: 26px; font-size: 15px; }
  .wordmark {
    position: absolute; display: flex; align-items: center; gap: 16px;
    color: var(--ink); font-weight: 400; letter-spacing: 2px;
    white-space: nowrap;
  }
  .wordmark-square { background: var(--ink); flex: none; }
  .card--contact .wordmark { right: 60px; bottom: 84px; font-size: 34px; }
  .card--contact .wordmark-square { width: 34px; height: 34px; }

  /* Front: brand card */
  .card--brand {
    top: 470px;
    background: linear-gradient(200deg, var(--blue-light), var(--blue-mid) 70%);
  }
  .card--brand .wordmark {
    left: 50%; top: 132px; transform: translateX(-50%);
    font-size: 46px;
  }
  .card--brand .wordmark-square { width: 44px; height: 44px; }
  .brand-band {
    position: absolute; left: 0; right: 0; bottom: 0; height: 44px;
    background: var(--ink);
    display: flex; align-items: center; justify-content: flex-start;
    padding: 0 36px 0 40px;
    font-family: "Roboto Condensed", "Arial Narrow", sans-serif;
    color: var(--band-text); font-size: 14px; letter-spacing: 0.2px;
    text-transform: uppercase;
    white-space: nowrap; overflow: hidden;
  }
</style>
</head>
<body>
<main class="sheet">

  <section class="card card--contact" aria-label="Contact side">
    <div class="contact-blue"></div>
    <div class="contact-info">
      <p class="contact-name">Ingrid Solberg</p>
      <p class="contact-title">Co-Founder &amp; CEO</p>
      <p class="contact-line">
        <svg viewBox="0 0 16 16" fill="none" stroke="currentColor" stroke-width="1.3"><rect x="4" y="1.5" width="8" height="13" rx="1.5"/><line x1="7" y1="12" x2="9" y2="12"/></svg>
        (047) 552-8190
      </p>
      <p class="contact-line">
        <svg viewBox="0 0 16 16" fill="none" stroke="currentColor" stroke-width="1.3"><rect x="1.5" y="3.5" width="13" height="9" rx="1"/><polyline points="1.5,4 8,9 14.5,4"/></svg>
        info@brensor.no
      </p>
      <p class="contact-line">
        <svg viewBox="0 0 16 16" fill="none" stroke="currentColor" stroke-width="1.2"><circle cx="8" cy="8" r="6.5"/><ellipse cx="8" cy="8" rx="3" ry="6.5"/><line x1="1.5" y1="8" x2="14.5" y2="8"/></svg>
        brensor.no
      </p>
      <p class="contact-address">Lindeholtveien 7 / 3142 Vestskogen</p>
    </div>
    <div class="wordmark"><span class="wordmark-square"></span><span>TALVIK BRENSOR</span></div>
  </section>

  <section class="card card--brand" aria-label="Brand side">
    <div class="wordmark"><span class="wordmark-square"></span><span>TALVIK BRENSOR</span></div>
    <p class="brand-band">Rental of qualified resources in software development, project management and IT operations</p>
  </section>

</main>
</body>
</html>
```